Plumbing Contractor Website Design

We are working with a Plumbing contractor in CA called KP Ductworks.

Some sites to use for content/competitors and inspiration:

https://www.pipelarkservice.example
https://www.drainowlpros.example
https://gantrybay.example/web/contractor/ (lots of contractor website designs we've approved and continue to show clients)

Thank you for taking the time to consider designing a website for us. We are web developers based in Stockton, CA, USA. Most of our projects go through the same process. Understanding this process may help you win a project with us. We custom-code all of our websites in-house. We don’t have any requirements as to what tools you use for your design, but we prefer Figma files. For any design that we label as four-stars, we send it to the client for review. The client picks the final design they want us to use. Once we complete this process, we will continue to show additional clients all the four-star sites and purchase them later. Your designs will have multiple chances to sell. For better chances of success, we ask that you follow these guidelines.

IMAGES:
If you use any images or icons in the design, we ask that you have a link to the asset so we can purchase the image/icon. Most of the designs we submit do not have the customer’s images on them unless they have some great images. Be creative; show us the feeling you are trying to portray with your image choices. Use any royalty-free site you choose. We subscribe to Velmora and mainly use their images, but we can purchase images outside of Velmora.

PLEASE NOTE: we will not submit designs to clients with watermarks on the images.

FONTS:
We ask that you identify the fonts used in the design. This can be done in a message if you want. We typically use Zintari Fonts and Velmora Fonts.

CONTENT:
We're always open to different content and ideas. We often submit designs with stock images so the client can see our vision. We typically take pictures after the website launch to use their images with our vision. Lorem Ipsum is fine for paragraphs, but we ask that you write the headers in correct English. We want to be able to show the vision and identify the sections of the website.

INSPIRATION:
We typically add a couple of links in the brief of websites we like to help you get started in your design.

REVISIONS:
We do not often ask for revisions of the designs unless we see something in the design that may not appeal to the client. If there are slight changes that we want to make, we do that in the development process.

FEEDBACK:
We rarely give feedback on designs during the design process. We are working on many website projects and do not have the time to provide feedback. We usually respond if your request is well thought out and asks specific questions, but a note asking “feedback, please” usually goes unanswered

```html
<!DOCTYPE html>
<html lang="en">
<head>
<meta charset="utf-8">
<title>Tidewell Plumbing</title>
<link href="https://fonts.googleapis.com/css2?family=Catamaran:wght@600;700&family=Roboto:wght@400;500;700&display=swap" rel="stylesheet">
<style>
:root{
  --navy:#0b4a86;
  --navy-deep:#083a6b;
  --ink:#111111;
  --text:#333333;
  --muted:#555555;
  --grey-bg:#f2f2f2;
  --footer:#0c0c0c;
  --white:#ffffff;
  --star:#f5a623;
}
*{margin:0;padding:0;box-sizing:border-box}
html,body{width:1200px;height:4508px;overflow:hidden}
body{position:relative;background:var(--white);font-family:"Roboto",sans-serif;color:var(--text)}
.abs{position:absolute}
.heading{font-family:"Catamaran",sans-serif;font-weight:700;color:var(--ink);text-transform:uppercase;letter-spacing:.5px}
.section-title{position:absolute;left:0;width:1200px;text-align:center;font-size:44px;line-height:1}
.section-title::after{content:"";display:block;width:86px;height:4px;background:var(--navy);margin:8px auto 0}
.btn{position:absolute;display:flex;align-items:center;justify-content:center;border-radius:30px;font-size:15px;font-weight:700;text-transform:uppercase;letter-spacing:.2px}
.btn-solid{background:var(--navy);color:var(--white);box-shadow:0 0 0 3px var(--white),0 0 0 5px var(--navy)}
.btn-outline{border:2px solid var(--navy);color:var(--navy);background:var(--white)}
/* header */
.site-header{position:absolute;left:0;top:0;width:1200px;height:145px;background:var(--white);z-index:3}
.logo-disc{position:absolute;left:88px;top:-60px;width:206px;height:260px;border-radius:0 0 103px 103px;background:var(--white);z-index:4;display:flex;align-items:center;justify-content:center;padding-top:80px}
.logo-name{font-family:"Roboto",sans-serif;font-weight:700;font-size:19px;color:var(--navy);text-align:center;line-height:1.15}
.book-btn{left:600px;top:28px;width:236px;height:48px;font-size:14px}
.call-icon{left:852px;top:22px;width:60px;height:60px;border-radius:50%;background:var(--white);box-shadow:0 2px 8px rgba(0,0,0,.18);display:flex;align-items:center;justify-content:center}
.call-text{left:925px;top:28px}
.call-text small{display:block;font-size:12px;font-weight:700;color:var(--ink)}
.call-text strong{display:block;font-size:20px;color:var(--navy);margin-top:3px}
.main-nav{position:absolute;left:368px;top:104px;display:flex;gap:27px;font-size:14px;font-weight:500;color:var(--ink)}
.main-nav .active{color:var(--navy);border-bottom:2px solid var(--navy)}
/* hero */
.hero{position:absolute;left:0;top:145px;width:1200px;height:670px;overflow:hidden}
.hero-photo{position:absolute;inset:0;background:linear-gradient(100deg,#8a8f95 0%,#6e6a66 30%,#4a3f33 55%,#2b4c8c 75%,#1f3f7a 100%)}
.hero-shade{position:absolute;inset:0;background:rgba(0,0,0,.18)}
.hero-title{position:absolute;left:0;top:212px;width:1200px;text-align:center;color:var(--white);font-size:52px}
.hero-sub{position:absolute;left:0;top:283px;width:1200px;text-align:center;color:var(--white);font-size:20px;line-height:31px;font-weight:500}
.hero-btn{left:524px;top:368px;width:154px;height:48px;border:3px solid var(--white)}
.hero-dots{position:absolute;left:1139px;top:237px;display:flex;flex-direction:column;gap:15px}
.hero-dots span{width:14px;height:14px;border-radius:50%;border:2px solid var(--white)}
.hero-dots .on{background:var(--white)}
.hero-wave{position:absolute;left:0;bottom:0}
/* about */
.about-photo{left:110px;top:878px;width:446px;height:446px;border-radius:50%;background:linear-gradient(135deg,#d9d9d6,#a5a5a3 55%,#c46b45)}
.about-inset{left:379px;top:1108px;width:216px;height:216px;border-radius:50%;border:6px solid var(--white);background:linear-gradient(160deg,#dfe6ee,#4b86c6 55%,#2a3a55)}
.about-title{left:675px;top:915px;font-size:42px}
.about-title::after{content:"";display:block;width:166px;height:4px;background:var(--navy);margin-top:2px}
.about-copy{left:675px;top:995px;width:414px;font-size:15px;line-height:26px;text-align:justify}
.about-copy p+p{margin-top:10px}
.about-btn{left:677px;top:1242px;width:149px;height:48px}
/* services */
.services{position:absolute;left:0;top:1435px;width:1200px;height:740px;background:var(--grey-bg)}
.service-card{position:absolute;top:179px;width:304px;height:472px;background:var(--white);border-radius:14px;box-shadow:0 4px 14px rgba(0,0,0,.14);text-align:center}
.service-card .photo{position:absolute;left:8px;top:8px;width:288px;height:210px;border-radius:8px 8px 0 0}
.service-card .badge{position:absolute;left:108px;top:175px;width:88px;height:88px;border-radius:50%;border:5px solid var(--white);display:flex;align-items:center;justify-content:center}
.service-card h3{position:absolute;left:0;top:285px;width:100%;font-size:17px;font-weight:700;color:var(--ink)}
.service-card p{position:absolute;left:22px;top:319px;width:260px;font-size:14px;line-height:25px;color:var(--muted)}
.service-card .btn{left:79px;top:402px;width:146px;height:46px;font-size:14px}
.slider-arrow{position:absolute;width:32px;height:32px;border-radius:50%;display:flex;align-items:center;justify-content:center}
/* testimonials */
.testimonials{position:absolute;left:0;top:2175px;width:1200px;height:497px;background:linear-gradient(120deg,#0e4f8e,#0a4178 60%,#0c4a86)}
.testimonials .section-title{color:var(--white);top:76px}
.testimonials .section-title::after{background:var(--white)}
.quote-card{position:absolute;top:182px;width:408px;height:228px;background:var(--white);border-radius:24px}
.quote-card .avatar{position:absolute;left:-32px;top:58px;width:106px;height:106px;border-radius:50%;border:4px solid var(--white);box-shadow:0 2px 8px rgba(0,0,0,.2)}
.quote-card .qmark{position:absolute;left:82px;top:26px}
.quote-card p{position:absolute;left:82px;top:68px;width:302px;font-size:12.5px;line-height:22px;color:var(--ink)}
.quote-card .who{position:absolute;left:82px;top:163px;font-size:15px;font-weight:700;color:var(--ink)}
.quote-card .stars{position:absolute;left:82px;top:186px;font-size:11px;color:var(--star);letter-spacing:1px}
/* why */
.why-item{position:absolute;width:240px;text-align:center}
.why-item .ring{width:146px;height:146px;border-radius:50%;background:var(--navy);margin:0 auto;display:flex;align-items:center;justify-content:center}
.why-item .ring span{width:126px;height:126px;border-radius:50%;border:2px dashed rgba(255,255,255,.8);display:flex;align-items:center;justify-content:center}
.why-item h3{margin-top:34px;font-size:17px;font-weight:700;color:var(--ink)}
.why-item p{margin-top:14px;font-size:15px;line-height:25px;color:var(--muted)}
/* contact */
.contact-photo{left:101px;top:3526px;width:428px;height:428px;border-radius:50%;border:14px solid var(--navy);background:var(--white);padding:6px}
.contact-photo div{width:100%;height:100%;border-radius:50%;background:linear-gradient(135deg,#d8dde2,#8d9196 45%,#222 70%,#c2332b)}
.contact-form{position:absolute;left:590px;top:3512px;width:510px}
.field-label{position:absolute;font-size:14px;color:var(--ink)}
.field{position:absolute;height:38px;border:1px solid #e2e2e2;background:var(--white);box-shadow:0 1px 4px rgba(0,0,0,.08);font-size:12px;color:#888;padding:0 18px;display:flex;align-items:center}
.field.area{height:90px;align-items:flex-start;padding-top:12px}
/* footer */
.site-footer{position:absolute;left:0;top:4030px;width:1200px;height:478px}
.footer-logo{left:130px;top:4228px;width:140px;height:140px;border-radius:50%;background:var(--white);display:flex;align-items:center;justify-content:center;text-align:center}
.footer-col{position:absolute;top:4176px;color:var(--white)}
.footer-col h4{font-size:17px;font-weight:700;margin-bottom:22px}
.footer-col li{list-style:none;font-size:14px;height:43px;display:flex;align-items:flex-start;gap:22px}
.footer-col li::before{content:"";width:10px;height:10px;border-radius:50%;border:3px solid var(--navy);background:#3a7fd0;margin-top:3px}
.contact-row{display:flex;gap:24px;margin-bottom:22px}
.contact-row .ico{width:36px;height:36px;border-radius:50%;background:var(--white);flex:none;display:flex;align-items:center;justify-content:center}
.contact-row b{display:block;font-size:14px;margin-bottom:6px}
.contact-row span{font-size:11.5px;line-height:20px}
.footer-rule{left:110px;top:4445px;width:1090px;height:1px;background:#2c2c2c}
.copyright{left:0;top:4466px;width:1200px;text-align:center;font-size:12px;color:var(--white)}
.social{position:absolute;top:4455px;width:34px;height:34px;border-radius:50%;border:2px solid var(--navy)}
.social.on{background:var(--navy)}
</style>
</head>
<body>

<header class="site-header">
  <div class="logo-disc"><div class="logo-name">TIDEWELL<br>PLUMBING</div></div>
  <a class="btn btn-solid book-btn">Book an Appointment</a>
  <div class="abs call-icon">
    <svg width="28" height="28" viewBox="0 0 24 24"><path fill="#0b4a86" d="M6.6 10.8a15.1 15.1 0 0 0 6.6 6.6l2.2-2.2c.3-.3.7-.4 1-.2 1.1.4 2.3.6 3.6.6.6 0 1 .4 1 1V20c0 .6-.4 1-1 1A17 17 0 0 1 3 4c0-.6.4-1 1-1h3.5c.6 0 1 .4 1 1 0 1.3.2 2.5.6 3.6.1.3 0 .7-.2 1z"/></svg>
  </div>
  <div class="abs call-text"><small>CALL US:</small><strong>+1 (555) 010 2040</strong></div>
  <nav class="main-nav">
    <span class="active">HOME</span><span>RESIDENTIAL</span><span>COMMERCIAL</span><span>WHY US</span><span>ABOUT US</span><span>LATEST BLOG</span><span>CONTACT US</span>
  </nav>
</header>

<section class="hero">
  <div class="hero-photo" role="img" aria-label="Plumber in blue overalls fixing pipes under a sink"></div>
  <div class="hero-shade"></div>
  <h1 class="heading hero-title" style="color:#fff">Tidewell Plumbing</h1>
  <p class="hero-sub">Lorem ipsum dolor sit amet, consectetur adipiscing elit,<br>sed do eiusmod tempor incidiea.</p>
  <a class="btn btn-solid hero-btn" style="box-shadow:none">Get Started</a>
  <div class="hero-dots"><span></span><span class="on"></span><span></span><span></span></div>
  <svg class="hero-wave" width="1200" height="200" viewBox="0 0 1200 200">
    <path d="M0 60 Q600 300 1200 60 L1200 200 L0 200 Z" fill="#0b4a86"/>
    <path d="M0 80 Q600 290 1200 100 L1200 200 L0 200 Z" fill="#ffffff"/>
  </svg>
</section>

<div class="abs about-photo" role="img" aria-label="Hands tightening a chrome sink trap with a wrench"></div>
<div class="abs about-inset" role="img" aria-label="Two plumbers standing beside a service van"></div>
<h2 class="abs heading about-title">About Us</h2>
<div class="abs about-copy">
  <p>Lorem ipsum dolor sit amet, consectetur adipiscing elit, sed do eiusmod tempor incididunt ut labore et dolore magna aliqua. Ut enim ad minim veniam, quis nostrud exercitation ullamco laboris nisi ut aliquip ex ea commodo consequat duis aute irure dolor in reprehea.</p>
  <p>Lorem ipsum dolor sit amet, consectetur adipiscing elit, sed do eiusmod tempor incididunt ut labore et dolore magna aliqua ut enim ad minimea.</p>
</div>
<a class="btn btn-solid about-btn">Learn More</a>

<section class="services">
  <h2 class="heading section-title" style="top:84px">Our Services</h2>
  <div class="slider-arrow" style="left:40px;top:399px;background:#e3e3e3">
    <svg width="12" height="12" viewBox="0 0 12 12"><path d="M8 1 3 6l5 5" stroke="#111" stroke-width="2" fill="none"/></svg>
  </div>
  <div class="slider-arrow" style="left:1128px;top:399px;background:var(--navy)">
    <svg width="12" height="12" viewBox="0 0 12 12"><path d="M4 1l5 5-5 5" stroke="#fff" stroke-width="2" fill="none"/></svg>
  </div>

  <article class="service-card" style="left:110px">
    <div class="photo" role="img" aria-label="Worker cleaning a street drain with a hose" style="background:linear-gradient(160deg,#9aa39a,#5f6660 55%,#e07a2a)"></div>
    <div class="badge" style="background:#9a9a9a"><svg width="40" height="40" viewBox="0 0 40 40" fill="none" stroke="#fff" stroke-width="2"><path d="M6 34h28M10 34V14h8v20M18 22h14v12"/></svg></div>
    <h3>DRAIN CLEANING</h3>
    <p>Lorem ipsum dolor sit amet, consect adipiscing elit, sed do eiusmod tempor ipsum dolor incididunt.</p>
    <a class="btn btn-outline" style="border-color:#777;color:var(--navy)">Learn More</a>
  </article>
  <article class="service-card" style="left:448px">
    <div class="photo" role="img" aria-label="Plumber repairing pipes under a kitchen sink" style="background:linear-gradient(150deg,#c9ced6,#3f6fb4 55%,#2a3347)"></div>
    <div class="badge" style="background:var(--navy)"><svg width="40" height="40" viewBox="0 0 40 40" fill="none" stroke="#fff" stroke-width="2"><circle cx="20" cy="20" r="12"/><circle cx="20" cy="20" r="5"/></svg></div>
    <h3>PLUMBING REPAIRS</h3>
    <p>Lorem ipsum dolor sit amet, consect adipiscing elit, sed do eiusmod tempor ipsum dolor incididunt.</p>
    <a class="btn btn-solid" style="box-shadow:0 0 0 2px #fff,0 0 0 3px var(--navy)">Learn More</a>
  </article>
  <article class="service-card" style="left:786px">
    <div class="photo" role="img" aria-label="Technician fitting an outdoor sewer pipe" style="background:linear-gradient(150deg,#3a4f7a,#2d3a4a 45%,#c43a2a 70%,#7a9a5a)"></div>
    <div class="badge" style="background:#9a9a9a"><svg width="40" height="40" viewBox="0 0 40 40" fill="none" stroke="#fff" stroke-width="2"><path d="M12 14h16v8H12zM20 22v6M8 32c4-3 8 3 12 0s8 3 12 0"/></svg></div>
    <h3>SEWER LINE REPAIR</h3>
    <p>Lorem ipsum dolor sit amet, consect adipiscing elit, sed do eiusmod tempor ipsum dolor incididunt.</p>
    <a class="btn btn-outline" style="border-color:#777">Learn More</a>
  </article>
</section>

<section class="testimonials">
  <h2 class="heading section-title">What Our Customers Say</h2>
  <svg class="abs" style="left:38px;top:286px" width="40" height="24" viewBox="0 0 40 24"><path d="M38 12H3M13 2 3 12l10 10" stroke="#fff" stroke-width="2" fill="none"/></svg>
  <svg class="abs" style="left:1122px;top:286px" width="40" height="24" viewBox="0 0 40 24"><path d="M2 12h35M27 2l10 10-10 10" stroke="#fff" stroke-width="2" fill="none"/></svg>

  <div class="quote-card" style="left:178px">
    <div class="avatar" role="img" aria-label="Customer portrait" style="background:linear-gradient(160deg,#8fae6a,#b06a3a)"></div>
    <svg class="qmark" width="28" height="22" viewBox="0 0 28 22" fill="#0b4a86"><path d="M0 22V12C0 5 4 1 11 0v5c-3 1-5 3-5 6h5v11zM16 22V12c0-7 4-11 11-12v5c-3 1-5 3-5 6h5v11z"/></svg>
    <p>Lorem ipsum dolor sit amet, consectetur adipiscing elit, sed do eiusmod tempor incididunt ut labore et dolore magna aliqua. Ut enim ad minim veniam, qui nostrud exercitation ullamcoea.</p>
    <div class="who">- CAROLINA</div>
    <div class="stars">★★★★★</div>
  </div>
  <div class="quote-card" style="left:667px">
    <div class="avatar" role="img" aria-label="Customer portrait" style="background:linear-gradient(160deg,#e6e6e6,#9a9a9a)"></div>
    <svg class="qmark" width="28" height="22" viewBox="0 0 28 22" fill="#0b4a86"><path d="M0 22V12C0 5 4 1 11 0v5c-3 1-5 3-5 6h5v11zM16 22V12c0-7 4-11 11-12v5c-3 1-5 3-5 6h5v11z"/></svg>
    <p>Lorem ipsum dolor sit amet, consectetur adipiscing elit, sed do eiusmod tempor incididunt ut labore et dolore magna aliqua. Ut enim ad minim veniam, qui nostrud exercitation ullamcoea.</p>
    <div class="who">- CAROLINA</div>
    <div class="stars">★★★★★</div>
  </div>
</section>

<h2 class="heading section-title" style="top:2782px">Why Tidewell Plumbing?</h2>

<div class="why-item" style="left:102px;top:2877px">
  <div class="ring"><span><svg width="56" height="56" viewBox="0 0 56 56" fill="none" stroke="#fff" stroke-width="2"><rect x="10" y="24" width="36" height="22" rx="2"/><circle cx="36" cy="16" r="7"/><path d="M16 32h14M16 38h20"/></svg></span></div>
  <h3>LOREM IPSUM</h3>
  <p>Lorem ipsum dolor sit amet, consect adipiscing elit, sed do eiusmod tempor ipsum dolor sed incididunt.</p>
</div>
<div class="why-item" style="left:353px;top:2928px">
  <div class="ring"><span><svg width="56" height="56" viewBox="0 0 56 56" fill="none" stroke="#fff" stroke-width="2"><circle cx="28" cy="24" r="16"/><path d="M20 40l-4 12 12-5 12 5-4-12M22 26l5 5 8-10"/></svg></span></div>
  <h3>LOREM IPSUM</h3>
  <p>Lorem ipsum dolor sit amet, consect adipiscing elit, sed do eiusmod tempor ipsum dolor sed incididunt.</p>
</div>
<div class="why-item" style="left:605px;top:2877px">
  <div class="ring"><span><svg width="56" height="56" viewBox="0 0 56 56" fill="none" stroke="#fff" stroke-width="2"><rect x="14" y="8" width="24" height="34" rx="2"/><path d="M20 18h12M20 25h12M20 32h6"/><circle cx="38" cy="38" r="9"/><path d="M34 38l3 3 5-6"/></svg></span></div>
  <h3>LOREM IPSUM</h3>
  <p>Lorem ipsum dolor sit amet, consect adipiscing elit, sed do eiusmod tempor ipsum dolor sed incididunt.</p>
</div>
<div class="why-item" style="left:857px;top:2928px">
  <div class="ring"><span><svg width="56" height="56" viewBox="0 0 56 56" fill="none" stroke="#fff" stroke-width="2"><path d="M16 18 28 8l12 10v10H16z"/><path d="M8 36l10-6 8 4 8-4 14 8-10 8-8-4-8 4z"/></svg></span></div>
  <h3>LOREM IPSUM</h3>
  <p>Lorem ipsum dolor sit amet, consect adipiscing elit, sed do eiusmod tempor ipsum dolor sed incididunt.</p>
</div>

<h2 class="heading section-title" style="top:3410px">Contact Us</h2>
<div class="abs contact-photo"><div role="img" aria-label="Plumber with a tool belt holding a red pipe wrench"></div></div>

<form class="contact-form">
  <label class="field-label" style="left:0;top:0">Name</label>
  <div class="field" style="left:0;top:20px;width:250px">Your Name</div>
  <label class="field-label" style="left:259px;top:0">City/Town</label>
  <div class="field" style="left:259px;top:20px;width:251px">Your City/Town</div>
  <label class="field-label" style="left:0;top:84px">Email</label>
  <div class="field" style="left:0;top:104px;width:250px">Your Email</div>
  <label class="field-label" style="left:259px;top:84px">Phone</label>
  <div class="field" style="left:259px;top:104px;width:251px">Your Phone</div>
  <label class="field-label" style="left:0;top:168px">Choose Services</label>
  <div class="field" style="left:0;top:188px;width:510px;justify-content:space-between">Select<svg width="10" height="6" viewBox="0 0 10 6"><path d="M1 1l4 4 4-4" stroke="#333" fill="none" stroke-width="1.5"/></svg></div>
  <label class="field-label" style="left:0;top:252px">Comment</label>
  <div class="field area" style="left:0;top:272px;width:510px">Enter Your Comment</div>
  <a class="btn btn-solid" style="left:2px;top:392px;width:168px;height:48px">Send Message</a>
</form>

<footer class="site-footer">
  <svg class="abs" style="left:0;top:0" width="1200" height="478" viewBox="0 0 1200 478">
    <path d="M0 120 Q600 -110 1200 120 L1200 478 L0 478 Z" fill="#0b4a86"/>
    <path d="M0 140 Q600 -70 1200 140 L1200 478 L0 478 Z" fill="#0c0c0c"/>
  </svg>
</footer>
<div class="abs footer-logo"><span class="logo-name" style="font-size:16px">TIDEWELL<br>PLUMBING</span></div>

<div class="footer-col" style="left:380px">
  <h4>NAVIGATION</h4>
  <ul><li>Home</li><li>Residential</li><li>Commercial</li><li>Why Us</li><li>About Us</li></ul>
</div>
<div class="footer-col" style="left:593px">
  <h4>QUICK LINKS</h4>
  <ul><li>Latest Blog</li><li>Contact Us</li><li>Privacy Policy</li><li>Terms Of Use</li></ul>
</div>
<div class="footer-col" style="left:832px">
  <h4>CONTACT US</h4>
  <div class="contact-row">
    <div class="ico"><svg width="16" height="18" viewBox="0 0 16 20"><path fill="#0b4a86" d="M8 0a7 7 0 0 0-7 7c0 5 7 13 7 13s7-8 7-13a7 7 0 0 0-7-7zm0 10a3 3 0 1 1 0-6 3 3 0 0 1 0 6z"/></svg></div>
    <div><b>LOCATIONS:</b><span>465, Lorum Ipsum Dolore Sed Ameat,<br>United States</span></div>
  </div>
  <div class="contact-row">
    <div class="ico"><svg width="16" height="16" viewBox="0 0 24 24"><path fill="#0b4a86" d="M6.6 10.8a15.1 15.1 0 0 0 6.6 6.6l2.2-2.2c.3-.3.7-.4 1-.2 1.1.4 2.3.6 3.6.6.6 0 1 .4 1 1V20c0 .6-.4 1-1 1A17 17 0 0 1 3 4c0-.6.4-1 1-1h3.5c.6 0 1 .4 1 1 0 1.3.2 2.5.6 3.6.1.3 0 .7-.2 1z"/></svg></div>
    <div><b>PHONE:</b><span>+1 (555) 010 2040</span></div>
  </div>
  <div class="contact-row">
    <div class="ico"><svg width="16" height="12" viewBox="0 0 20 14"><path fill="#0b4a86" d="M0 0h20v14H0z"/><path d="M1 1l9 7 9-7" stroke="#fff" fill="none" stroke-width="1.5"/></svg></div>
    <div><b>EMAIL:</b><span>info@tidewellplumbing.example</span></div>
  </div>
</div>

<div class="abs footer-rule"></div>
<p class="abs copyright">© 2024 TIDEWELL PLUMBING &nbsp;|&nbsp; All Rights Reserved</p>
<span class="social" style="left:973px" aria-label="Social profile"></span>
<span class="social on" style="left:1014px" aria-label="Social profile"></span>
<span class="social" style="left:1055px" aria-label="Social profile"></span>

</body>
</html>
```